Book cover design for a collection of poetry - The Lanternfield

Book cover and back design need to be moody, nostalgic, reflective, ethereal. Melancholy and other worldly. Cover design should not be time specific to a period or place but if applicable should reflect British landscape. Book cover should be in tones of blue and must include the title and author (THE LANTERNFIELD BY DORIAN WELKBRIDGE). We love the idea of rain, and looking out of a window. See attached designs. A world you are observing but not in.

Industry/Entity Type

Book Publisher

Font styles to use
Serif
Script

Colors
3176b5
3377b5
85acd3
eaf1f7
0792cd
33a6d7
86cae7
ecf7fb
86cfc6

Requirements
Must have
• The colour blue in it, must be melancholy and reflective.
Nice to have
• Rain in the cover.
Should not have
• Any bright colours.

```html
<!DOCTYPE html>
<html lang="en">
<head>
<meta charset="utf-8">
<title>The Lanternfield — Back Cover</title>
<link rel="stylesheet" href="https://fonts.googleapis.com/css2?family=Cormorant+Garamond:wght@400;500&family=Josefin+Slab:wght@400&display=swap">
<style>
  :root {
    --blue-deep: #245a92;
    --blue-mid: #2773b5;
    --blue-soft: #3377b5;
    --trunk: rgba(24, 70, 125, 0.45);
    --mist: rgba(120, 170, 215, 0.18);
    --ink-light: #eaf1f7;
  }
  * { margin: 0; padding: 0; box-sizing: border-box; }
  html, body { width: 754px; height: 1200px; overflow: hidden; }
  body { background: var(--blue-mid); }
  .back-cover {
    position: relative;
    width: 754px;
    height: 1200px;
    overflow: hidden;
    color: var(--ink-light);
    text-align: center;
  }
  .forest-backdrop {
    position: absolute;
    inset: 0;
    background:
      radial-gradient(ellipse 60% 35% at 60% 20%, var(--mist), rgba(0,0,0,0) 70%),
      linear-gradient(90deg,
        var(--trunk) 0%, rgba(0,0,0,0) 6%,
        rgba(0,0,0,0) 10%, var(--trunk) 12%, var(--trunk) 15%, rgba(0,0,0,0) 18%,
        rgba(0,0,0,0) 26%, var(--trunk) 28%, var(--trunk) 31%, rgba(0,0,0,0) 33%,
        rgba(0,0,0,0) 46%, var(--trunk) 48%, var(--trunk) 53%, rgba(0,0,0,0) 55%,
        rgba(0,0,0,0) 60%, var(--trunk) 62%, var(--trunk) 65%, rgba(0,0,0,0) 67%,
        rgba(0,0,0,0) 90%, var(--trunk) 94%, var(--trunk) 97%, rgba(0,0,0,0) 100%),
      linear-gradient(180deg, var(--blue-soft) 0%, var(--blue-mid) 45%, var(--blue-deep) 100%);
  }
  .title {
    position: absolute;
    top: 122px;
    left: 0;
    width: 100%;
    font-family: "Cormorant Garamond", serif;
    font-weight: 400;
    font-size: 66px;
    line-height: 1;
    letter-spacing: 0;
    white-space: nowrap;
  }
  .title .article {
    font-size: 18px;
    vertical-align: 22px;
    margin-right: 3px;
  }
  .author {
    position: absolute;
    top: 212px;
    left: 0;
    width: 100%;
    font-family: "Cormorant Garamond", serif;
    font-weight: 500;
    font-size: 19px;
    letter-spacing: 8px;
  }
  .rule {
    position: absolute;
    left: 167px;
    width: 422px;
    height: 1.5px;
    background: linear-gradient(90deg, rgba(234,241,247,0) 0%, var(--ink-light) 12%, var(--ink-light) 88%, rgba(234,241,247,0) 100%);
  }
  .rule--top { top: 275px; }
  .rule--bottom { top: 767px; }
  .blurb-heading {
    position: absolute;
    top: 320px;
    left: 0;
    width: 100%;
    font-family: "Cormorant Garamond", serif;
    font-weight: 500;
    font-size: 21px;
    letter-spacing: 0.4px;
  }
  .blurb {
    position: absolute;
    left: 30px;
    width: 694px;
    font-family: "Josefin Slab", serif;
    font-weight: 400;
    font-size: 19px;
    line-height: 30.8px;
    letter-spacing: 0.7px;
    white-space: nowrap;
  }
  .blurb--story { top: 372px; }
  .blurb--themes { top: 618px; }
</style>
</head>
<body>
  <main class="back-cover">
    <div class="forest-backdrop" role="img" aria-label="Misty blue forest of tall tree trunks fading into fog"></div>

    <h1 class="title"><span class="article">THE</span>LANTERNFIELD</h1>
    <p class="author">BY DORIAN WELKBRIDGE</p>

    <div class="rule rule--top"></div>

    <h2 class="blurb-heading">THE LANTERNFIELD IS A COLLECTION OF POETRY.</h2>

    <p class="blurb blurb--story">
      Told in two parts we first meet charles – aged, crippled and<br>
      left alone in his inherited marsh house - reflecting on his life<br>
      and his marriage to beautiful alice who we meet inpart two.<br>
      Alice is suicidal, manically depressed and struggling with life<br>
      as a wife and mother. She meets, harbors and falls in love<br>
      with a soldier during wwii and her world is changed<br>
      Forever.
    </p>

    <p class="blurb blurb--themes">
      Moving through the 20th century, this life and the next, the<br>
      lanternfield interweaves grief, loss, the after-life, mental illness,<br>
      and ultimately the true nature of love.
    </p>

    <div class="rule rule--bottom"></div>
  </main>
</body>
</html>
```